We need visit card and a letter paper for our website. thx

We have a beauty clinic in Switzerland.
https://wolkenbachtal.ch
We need a visit card.

Requirements
Must have
• see colors on website

```html
<!DOCTYPE html>
<html lang="de">
<head>
<meta charset="utf-8">
<title>Wolkenbachtal – Visitenkarte</title>
<link rel="stylesheet" href="https://fonts.googleapis.com/css2?family=Fira+Sans:wght@300;400;500&display=swap">
<style>
  :root {
    --backdrop: #d3d8d8;
    --paper: #f1f1ef;
    --ink: #1b1b1b;
    --ink-soft: #6a6a6a;
    --card-dark: #141414;
    --on-dark: #ffffff;
  }
  * { margin: 0; padding: 0; box-sizing: border-box; }
  html, body {
    width: 1200px;
    height: 852px;
    overflow: hidden;
    background: var(--backdrop);
    font-family: "Fira Sans", sans-serif;
  }
  .sheet {
    width: 1200px;
    height: 852px;
    display: flex;
    align-items: center;
    justify-content: center;
    gap: 60px;
  }
  .card {
    width: 510px;
    height: 330px;
    border-radius: 3px;
    box-shadow: 0 10px 28px rgba(0, 0, 0, 0.16);
    display: flex;
    flex-direction: column;
    align-items: center;
    justify-content: center;
    text-align: center;
  }
  .card--contact {
    background: var(--paper);
    color: var(--ink);
  }
  .card--brand {
    background: var(--card-dark);
    color: var(--on-dark);
  }
  .contact__names {
    font-size: 16px;
    font-weight: 400;
    letter-spacing: 0.2px;
  }
  .contact__rule {
    width: 210px;
    height: 2px;
    background: var(--ink);
    margin: 16px 0 18px;
  }
  .contact__line {
    font-size: 15px;
    font-weight: 300;
    line-height: 1.5;
    color: var(--ink-soft);
  }
  .contact__line b {
    font-weight: 500;
    color: var(--ink);
  }
  .contact__web {
    font-size: 15px;
    font-weight: 500;
    line-height: 1.5;
    color: var(--ink);
  }
  .brand {
    display: flex;
    align-items: center;
    gap: 16px;
  }
  .brand__mark {
    width: 14px;
    height: 14px;
    background: var(--on-dark);
  }
  .brand__name {
    font-size: 44px;
    font-weight: 400;
    letter-spacing: 0.5px;
  }
</style>
</head>
<body>
  <main class="sheet">
    <section class="card card--contact" aria-label="Visitenkarte Rückseite">
      <p class="contact__names">Dr. Lena Hofstetter | Dr. Markus Reinalter, DESA</p>
      <div class="contact__rule"></div>
      <p class="contact__line">Talstrasse 22, 7550 Wolkenbach, Switzerland</p>
      <p class="contact__line"><b>P:</b> +41 (0) 800 24 68 20 | <b>E:</b> hallo@wolkenbachtal.ch</p>
      <p class="contact__web">wolkenbachtal.ch</p>
    </section>
    <section class="card card--brand" aria-label="Visitenkarte Vorderseite">
      <div class="brand">
        <span class="brand__mark"></span>
        <span class="brand__name">Wolkenbachtal</span>
      </div>
    </section>
  </main>
</body>
</html>
```